METAL FABRICATION BUSINESS CARD

** I will be ending the project and picking design early. This Friday October 3rd at 7am MST if not sooner**
ONE SIDED BUSINESS CARD ONLY. AND LOGO SIZE TO BE DOMINANT so it stands out.
Looking for a black background and will be doing raised chrome/silver font on the business cards. Looking to have the following on the front of the business card. Company logo is uploaded in files.
Company logo
*Compartment Doors
*Roof Radius Metal
*J-Wrap Metal Skirting
*S-Lock Beltline Molding
*Pre-Bent Molding
and more...
Owen Daltry 307.552.4198 info@KX-Welt.com
Updates
One sided business card only please. Also logo size should be dominant and sized bigger
Contact Information for Business Card
Black background, Text will be raised chrome/silver, and corners will be rounded.

```html
<!DOCTYPE html>
<html lang="en">
<head>
<meta charset="utf-8">
<title>KX-Welt Business Card</title>
<link rel="stylesheet" href="https://fonts.googleapis.com/css2?family=Michroma&display=swap">
<style>
  :root {
    --backdrop: #2b2b2b;
    --card-black: #1c1c1e;
    --chrome: #dcdcdc;
    --chrome-soft: #c4c4c4;
  }
  * { margin: 0; padding: 0; box-sizing: border-box; }
  html, body {
    width: 1200px;
    height: 900px;
    overflow: hidden;
    background: var(--backdrop);
  }
  .business-card {
    position: absolute;
    left: 110px;
    top: 170px;
    width: 980px;
    height: 560px;
    border-radius: 36px;
    background: var(--card-black);
    font-family: "Michroma", sans-serif;
    color: var(--chrome);
  }
  .brand-name {
    position: absolute;
    right: 64px;
    top: 70px;
    font-size: 104px;
    line-height: 1;
    letter-spacing: 2px;
    color: var(--chrome);
  }
  .contact {
    position: absolute;
    left: 64px;
    top: 240px;
  }
  .contact-name {
    font-size: 26px;
    letter-spacing: 1px;
    margin-bottom: 34px;
  }
  .contact-line {
    font-size: 23px;
    line-height: 1.35;
    color: var(--chrome-soft);
  }
  .services {
    position: absolute;
    right: 64px;
    top: 300px;
    list-style: none;
    font-size: 22px;
    line-height: 1.55;
    color: var(--chrome-soft);
  }
  .services li::before {
    content: "\2022\00a0";
  }
  .services .more::before { content: ""; }
</style>
</head>
<body>
  <article class="business-card">
    <div class="brand-name">KX-Welt</div>

    <section class="contact">
      <p class="contact-name">Owen Daltry</p>
      <p class="contact-line">307.552.4198</p>
      <p class="contact-line">info@KX-Welt.com</p>
    </section>

    <ul class="services">
      <li>Compartment Doors</li>
      <li>Roof Radius Metal</li>
      <li>J-Wrap Metal Skirting</li>
      <li>S-Lock Beltline Molding</li>
      <li>Pre-Bent Molding</li>
      <li class="more">and more...</li>
    </ul>
  </article>
</body>
</html>
```